Need to create a website for a luxury custom home builder in Phoenix USA. Looking forward for some creative designs including a full page video intro on homepage and should show up pretty luxurious.

```html
<!DOCTYPE html>
<html lang="en">
<head>
<meta charset="UTF-8">
<title>Mesa Crest Homes — Luxury Custom Homes in Phoenix</title>
<link rel="stylesheet" href="https://fonts.googleapis.com/css2?family=Inter:wght@500;600;700&display=swap">
<style>
  :root {
    --nav-bg: #f7f7f7;
    --ink: #111111;
    --ink-soft: #2a2a2a;
    --brand-blue: #1e90d8;
    --brand-teal: #14a98c;
    --teal-dark: #0f8f83;
    --field-bg: #e6e6e6;
    --field-border: #bdbdbd;
    --label: #5a5a5a;
    --panel-bg: rgba(245, 247, 244, 0.72);
    --photo-green: #7f9a5a;
    --photo-light: #e9eeee;
    --white: #ffffff;
  }
  * { box-sizing: border-box; margin: 0; padding: 0; }
  html, body {
    width: 1200px; height: 683px; overflow: hidden;
    font-family: "Inter", Arial, sans-serif;
    background: var(--white);
  }
  .site { width: 1200px; height: 683px; position: relative; }

  .site-header {
    height: 76px; background: var(--nav-bg);
    position: relative; display: flex; align-items: center;
  }
  .brand {
    position: absolute; left: 183px; top: 24px;
    display: flex; align-items: center; gap: 10px;
    font-weight: 700; font-size: 20px; color: var(--brand-teal);
    letter-spacing: 0.3px;
  }
  .brand-dot { width: 26px; height: 26px; border-radius: 50%; background: var(--brand-blue); }
  .main-nav { position: absolute; left: 460px; top: 0; height: 76px; display: flex; align-items: center; gap: 0; }
  .main-nav a {
    font-weight: 600; font-size: 16.5px; color: var(--ink); text-decoration: none;
    display: flex; align-items: center; gap: 4px; position: absolute; white-space: nowrap;
  }
  .nav-listings { left: 0; }
  .nav-pricing { left: 131px; }
  .nav-about { left: 237px; }
  .quote-btn {
    position: absolute; left: 872px; top: 13px; width: 145px; height: 50px;
    border-radius: 25px; background: var(--brand-blue); color: var(--white);
    font-weight: 600; font-size: 16.5px; display: flex; align-items: center; justify-content: center;
    text-decoration: none;
  }

  .hero { position: relative; height: 607px; overflow: hidden; }
  .hero-photo {
    position: absolute; inset: 0;
    background:
      radial-gradient(ellipse 55% 45% at 30% 20%, rgba(111, 140, 70, 0.75), transparent 70%),
      radial-gradient(ellipse 40% 35% at 85% 15%, rgba(120, 110, 80, 0.6), transparent 70%),
      linear-gradient(180deg, var(--photo-green) 0%, #c9d3c2 35%, var(--photo-light) 70%, #f3f6f7 100%);
  }
  .hero-veil {
    position: absolute; inset: 0;
    background: linear-gradient(90deg, rgba(255,255,255,0.55) 0%, rgba(255,255,255,0.35) 50%, rgba(255,255,255,0.15) 100%);
  }
  .hero-copy { position: absolute; left: 169px; top: 138px; }
  .hero-title {
    font-weight: 700; font-size: 49px; line-height: 57px; color: var(--ink); letter-spacing: -0.3px;
  }
  .hero-sub {
    margin-top: 20px; font-weight: 600; font-size: 19px; line-height: 25px; color: var(--ink-soft);
    width: 480px;
  }
  .explore-btn {
    display: inline-flex; align-items: center; justify-content: center;
    margin-top: 36px; width: 175px; height: 50px; border-radius: 25px;
    background: var(--brand-teal); color: var(--white); font-weight: 600; font-size: 16.5px;
    text-decoration: none;
  }

  .lead-form {
    position: absolute; left: 735px; top: 52px; width: 308px; height: 394px;
    background: var(--panel-bg); border-radius: 4px;
    box-shadow: 0 2px 10px rgba(0,0,0,0.08);
    padding: 50px 0 0 46px;
  }
  .form-badge {
    position: absolute; right: -24px; top: -24px; width: 48px; height: 48px; border-radius: 50%;
    background: #9a9a9a; border: 2px solid #d8d8d8;
    display: flex; align-items: center; justify-content: center;
  }
  .field { margin-bottom: 19px; }
  .field-label {
    display: flex; align-items: center; gap: 6px;
    font-weight: 600; font-size: 16px; color: var(--label); margin-bottom: 6px;
  }
  .field-icon { width: 20px; height: 20px; border-radius: 50%; background: #6b6b6b; display: flex; align-items: center; justify-content: center; }
  .field-input {
    width: 210px; height: 44px; background: var(--field-bg);
    border: 1px solid var(--field-border); border-radius: 3px;
    box-shadow: inset 0 1px 3px rgba(0,0,0,0.12);
    font-family: "Inter", Arial, sans-serif; font-size: 16px; padding-left: 22px; color: #888;
  }
  .field-input::placeholder { color: #9a9a9a; }
  .priority-btn {
    margin: 10px 0 0 5px; width: 202px; height: 44px; border-radius: 22px;
    border: 2px solid #8fd6c9;
    background: linear-gradient(180deg, var(--brand-teal), var(--teal-dark));
    color: var(--white); font-family: "Inter", Arial, sans-serif; font-weight: 700; font-size: 16px;
  }
</style>
</head>
<body>
<div class="site">
  <header class="site-header">
    <a class="brand" href="#"><span class="brand-dot"></span>Mesa Crest Homes</a>
    <nav class="main-nav">
      <a class="nav-listings" href="#">Listings
        <svg width="14" height="14" viewBox="0 0 14 14"><path d="M3 5l4 4 4-4" fill="none" stroke="#555" stroke-width="1.5"/></svg>
      </a>
      <a class="nav-pricing" href="#">Pricing</a>
      <a class="nav-about" href="#">About</a>
    </nav>
    <a class="quote-btn" href="#">Get A Quote</a>
  </header>

  <section class="hero">
    <div class="hero-photo" role="img" aria-label="Aerial view of modern white luxury homes with green gardens in Phoenix"></div>
    <div class="hero-veil"></div>

    <div class="hero-copy">
      <h1 class="hero-title">Crafting Dreams.<br>Building Homes.<br>Fulfilling Visions.</h1>
      <p class="hero-sub">Luxury Custom Homes for Sale: Elevating Living in Phoenix, One Dream Home at a Time.</p>
      <a class="explore-btn" href="#">Explore Listings</a>
    </div>

    <form class="lead-form">
      <span class="form-badge">
        <svg width="26" height="26" viewBox="0 0 24 24"><path d="M12 2l3 6.5 7 .8-5.2 4.8 1.4 7-6.2-3.6-6.2 3.6 1.4-7L2 9.3l7-.8z" fill="#e4e4e4"/></svg>
      </span>
      <div class="field">
        <label class="field-label"><span class="field-icon"><svg width="12" height="12" viewBox="0 0 12 12"><circle cx="6" cy="4" r="2.2" fill="#fff"/><path d="M2 11c0-2.5 2-4 4-4s4 1.5 4 4z" fill="#fff"/></svg></span>Name:</label>
        <input class="field-input" type="text" placeholder="Name">
      </div>
      <div class="field">
        <label class="field-label"><span class="field-icon"><svg width="12" height="12" viewBox="0 0 12 12"><rect x="1.5" y="3" width="9" height="6.5" fill="none" stroke="#fff" stroke-width="1.2"/><path d="M1.5 3l4.5 3.5L10.5 3" fill="none" stroke="#fff" stroke-width="1.2"/></svg></span>Email:</label>
        <input class="field-input" type="email" placeholder="Email">
      </div>
      <div class="field">
        <label class="field-label"><span class="field-icon"><svg width="12" height="12" viewBox="0 0 12 12"><path d="M3 1.5l1.8 2.2-1 1.3c.6 1.3 1.6 2.3 2.9 2.9l1.3-1 2.2 1.8-1 1.8C5.5 10.3 1.7 6.5 1.2 2.5z" fill="#fff"/></svg></span>Phone:</label>
        <input class="field-input" type="tel" placeholder="Phone">
      </div>
      <button class="priority-btn" type="button">Get Priority Access</button>
    </form>
  </section>
</div>
</body>
</html>
```